Dog Snacks brand needs a new packaging design

Dear Designers,

We are looking for a packaging expert to design our new line of Dog Snacks which contain a relaxing hemp extract (CBD).

Our company is already selling various relaxing cat & dog products , and we would like this new design to reflect the same "style & feeling" as our current products (see attached instructions).

Technical aspects:
- The packaging is a Stand Up Pouch (12x18.5x7cm - see attached instructions).
- Please follow technical guidelines from printer (see attached instructions).
- The packaging will contain 120g of high-quality, semi-moist dog snacks.
- We will be designing 3 differents variations for 3 different flavours: Chicken, Beef & Liver.
- The packaging will be printed with a matt finish.

Design aspects:
- The design should be compatible with our brand identity (i.e. fluffly, pure, relaxing, positive, clean & natural).
- Soft/rounded shapes are preferred.
- Please use our brand's colors (#3BA384, White & Black).
- Please use our company logo (see attached instructions).
- The design also needs to convey a strong sense of professionalism as we are an animal "healthcare" brand.
- If you want to include a dog picture, we would prefer you to use a picture of our official brand ambassador (see attached instructions).
- We have attached a number of packaging examples which we like a lot. (see attached instructions). Please only use those as general inspiration.
- Only original work (no plagiarism will be accepted).

Please don't hesitate to send us a message if you have any questions about the brand, the product or the design requirements.

We look forward to seeing your designs & working on this together !

Thanks & regards,
Marcus

Dog owners

Pet Care

Sans Serif

• Please see project description.

```html
<!DOCTYPE html>
<html lang="en">
<head>
<meta charset="utf-8">
<title>Verdalis CBD Treats – Chicken Flavor Pouch</title>
<link rel="stylesheet" href="https://fonts.googleapis.com/css2?family=Anton&family=Oswald:wght@400;500;600&family=Marcellus&family=Roboto:wght@400&display=swap">
<style>
  :root {
    --brand-green: #3ba384;
    --brand-green-deep: #2f8f72;
    --brand-green-pale: #d7ede5;
    --ink: #111111;
    --white: #ffffff;
    --pouch-grey: #ececee;
    --paw-grey: #d3d4d7;
    --badge-blue: #3a4f8f;
    --badge-gold: #b9a880;
  }
  * { margin: 0; padding: 0; box-sizing: border-box; }
  html, body {
    width: 1200px; height: 1132px; overflow: hidden;
    background: var(--white);
  }
  .canvas { position: relative; width: 1200px; height: 1132px; }

  .pouch {
    position: absolute; left: 296px; top: 118px;
    width: 505px; height: 922px;
    background: linear-gradient(180deg, #ffffff 0%, #f7f7f8 55%, var(--pouch-grey) 100%);
    overflow: hidden;
  }
  .pouch > * { position: absolute; }

  .brand-strip {
    left: 150px; top: 0; width: 117px; height: 215px;
    background: linear-gradient(180deg, var(--brand-green) 0%, #8fcab5 55%, var(--brand-green-pale) 100%);
    border: 2px solid #2b3a33; border-top: none;
  }
  .paw-decoration {
    left: 30px; top: 91px; width: 266px; height: 260px;
    border-radius: 48% 52% 46% 54% / 50% 44% 56% 50%;
    background: radial-gradient(circle at 60% 60%, var(--paw-grey) 0%, #e1e2e4 70%, rgba(230,230,232,0) 100%);
  }
  .brand-oval {
    left: 115px; top: 60px; width: 194px; height: 128px;
    border-radius: 50%;
    background: var(--white);
    border: 3px solid #2e2e2e;
    box-shadow: 0 7px 0 #3a3a3a;
    display: flex; align-items: center; justify-content: center;
  }
  .brand-name {
    font-family: "Oswald", sans-serif; font-weight: 500;
    font-size: 26px; letter-spacing: 2px; color: var(--ink);
  }
  .vet-seal {
    left: 372px; top: 103px; width: 88px; height: 88px;
    border-radius: 50%;
    background: var(--white);
    border: 4px dotted var(--badge-gold);
    box-shadow: inset 0 0 0 6px var(--white), inset 0 0 0 8px var(--badge-blue);
  }
  .ambassador-photo {
    left: 215px; top: 257px; width: 300px; height: 484px;
    border-radius: 44% 0 0 50% / 30% 0 0 40%;
    background: linear-gradient(160deg, #e8e6e6 0%, #c9c5c6 45%, #a9a4a6 75%, #dcdada 100%);
  }
  .flavor-band {
    left: 0; top: 440px; width: 260px; height: 232px;
    background: linear-gradient(90deg, var(--brand-green-deep) 0%, var(--brand-green) 55%, #6dbb9f 100%);
  }
  .line-name {
    left: 76px; top: 462px;
    font-family: "Oswald", sans-serif; font-weight: 400;
    font-size: 36px; line-height: 1; letter-spacing: 0.5px;
    color: var(--white);
    -webkit-text-stroke: 1px #2a2a2a;
    transform: scaleX(0.85); transform-origin: left;
  }
  .line-name sup { font-size: 12px; -webkit-text-stroke: 0; vertical-align: top; }
  .product-title {
    left: 18px; top: 530px;
    font-family: "Anton", sans-serif;
    font-size: 70px; line-height: 1; letter-spacing: 1px;
    color: var(--ink);
    -webkit-text-stroke: 2px var(--white);
    paint-order: stroke fill;
    white-space: nowrap;
  }
  .dose {
    left: 104px; top: 611px;
    font-family: "Roboto", sans-serif; font-size: 20px; letter-spacing: 1px;
    color: var(--ink);
  }
  .thc-seal {
    left: 127px; top: 650px; width: 76px; height: 76px;
    border-radius: 50%;
    border: 3px dotted var(--brand-green);
  }
  .flavor-icon {
    left: 45px; top: 730px; width: 40px; height: 36px;
    border-radius: 40% 50% 30% 30%;
    background: linear-gradient(135deg, var(--brand-green) 0%, var(--brand-green-deep) 100%);
  }
  .flavor-name {
    left: 15px; top: 770px; width: 112px;
    font-family: "Marcellus", serif; color: var(--ink); text-align: center;
    line-height: 1.05;
  }
  .flavor-name .flavor-main { display: block; font-size: 23px; }
  .flavor-name .flavor-sub { display: block; font-size: 20px; margin-left: -12px; }
  .diet-seal {
    top: 780px; width: 46px; height: 46px; border-radius: 50%;
    border: 2px solid var(--brand-green);
    box-shadow: inset 0 0 0 5px var(--white), inset 0 0 0 6px var(--brand-green);
  }
  .diet-seal.gluten { left: 384px; }
  .diet-seal.gmo { left: 445px; }
  .benefits {
    left: 0; width: 505px; top: 828px; text-align: center;
    padding-left: 2px;
    font-family: "Oswald", sans-serif; font-weight: 500;
    font-size: 21px; letter-spacing: 2px; color: var(--ink);
  }
  .net-band {
    left: 0; top: 877px; width: 505px; height: 45px;
    background: linear-gradient(180deg, #a9d6c6 0%, #7cc0a8 45%, var(--brand-green) 100%);
    display: flex; align-items: center; justify-content: center;
    font-family: "Oswald", sans-serif; font-weight: 500;
    font-size: 19px; color: var(--ink);
  }
</style>
</head>
<body>
<main class="canvas">
  <section class="pouch" aria-label="Verdalis CBD treats pouch, front">
    <div class="paw-decoration" role="img" aria-label="Large soft grey paw print decoration"></div>
    <div class="brand-strip"></div>
    <div class="brand-oval">
      <span class="brand-name">VERDALIS</span>
    </div>
    <div class="vet-seal" role="img" aria-label="Veterinary recommendation seal"></div>

    <div class="ambassador-photo" role="img" aria-label="Photo of the brand ambassador dog wearing round glasses and a bow tie"></div>

    <div class="flavor-band"></div>
    <h2 class="line-name">VerdaBites<sup>TM</sup></h2>
    <h1 class="product-title">CBD TREATS</h1>
    <p class="dose">CBD 250mg</p>
    <div class="thc-seal" role="img" aria-label="THC free seal"></div>

    <div class="flavor-icon" role="img" aria-label="Chicken illustration"></div>
    <p class="flavor-name"><span class="flavor-main">CHICKEN</span><span class="flavor-sub">Flavor</span></p>

    <div class="diet-seal gluten" role="img" aria-label="Gluten free seal"></div>
    <div class="diet-seal gmo" role="img" aria-label="GMO free seal"></div>

    <p class="benefits">SUPPORT | CALM | EASE</p>
    <div class="net-band">Net wt: 120g</div>
  </section>
</main>
</body>
</html>
```